Stikers for GPS tracking company

I would like to have a sticker designed that my customers put on their vehicles and machines, to show that they have a Gps Tracking Alarm installed in their vehicle or machine.

Like stickers you use and put in your window in your home to show you have video surveillance system installed in your house.

It should be 10 cm high and 7 cm wide.

I have attached a version i have made myself, but im not satisfied with it

Target Market(s)

This is stickers that will sit on my customers assets, so the Volmira logo should be less visible and large,

Industry/Entity Type

GPS tracking and fleet management

Font styles to use
Sans Serif

Colors
0054AA
0677BA
7BADD7
CADEEF
E8F1F8

Requirements
Must have
• There should be an indication of location awareness

```html
<!DOCTYPE html>
<html lang="en">
<head>
<meta charset="UTF-8">
<title>Volmira GPS Tracking Alarm Stickers</title>
<link rel="stylesheet" href="https://fonts.googleapis.com/css2?family=Barlow+Semi+Condensed:wght@700&display=swap">
<style>
  :root {
    --page: #ffffff;
    --sticker-edge: #dcdcdc;
    --navy: #122e57;
    --sky-top: #cadeef;
    --sky-mid: #b4d3f1;
    --sky-bottom: #90c1ee;
    --accent-deep: #2563eb;
    --accent-bright: #22a3ee;
    --ring: rgba(255, 255, 255, 0.75);
    --ring-soft: rgba(255, 255, 255, 0.35);
    --halo: rgba(63, 130, 220, 0.22);
  }
  * { margin: 0; padding: 0; box-sizing: border-box; }
  html, body {
    width: 1200px;
    height: 900px;
    overflow: hidden;
    background: var(--page);
  }
  .sheet {
    position: relative;
    width: 1240px;
    height: 930px;
    transform: scale(0.968);
    transform-origin: 0 0;
  }
  .sticker {
    position: absolute;
    top: 170px;
    width: 412px;
    height: 590px;
    background: #fff;
    border: 1px solid var(--sticker-edge);
    border-radius: 48px;
    font-family: "Barlow Semi Condensed", "Arial Narrow", sans-serif;
    font-weight: 700;
    color: var(--navy);
  }
  .sticker--deep { left: 178px; --accent: var(--accent-deep); }
  .sticker--bright { left: 650px; --accent: var(--accent-bright); }
  .sticker__panel {
    position: absolute;
    left: 14px;
    top: 14px;
    width: 384px;
    height: 561px;
    border-radius: 36px;
    overflow: hidden;
  }
  .sticker__map {
    position: absolute;
    inset: 0;
    background: linear-gradient(180deg, var(--sky-top) 0%, var(--sky-mid) 45%, var(--sky-bottom) 100%);
  }
  .sticker__signal {
    position: absolute;
    inset: 0;
  }
  .brand {
    position: absolute;
    left: 85px;
    top: 49px;
    display: flex;
    align-items: center;
    gap: 14px;
  }
  .brand__square {
    width: 36px;
    height: 36px;
    border-radius: 5px;
    background: var(--accent);
  }
  .brand__name {
    font-size: 44px;
    line-height: 1;
    color: var(--navy);
  }
  .headline {
    position: absolute;
    left: 0;
    width: 384px;
    text-align: center;
    line-height: 1;
  }
  .headline--gps { top: 161px; font-size: 128px; letter-spacing: 1px; }
  .headline--tracking { top: 277px; font-size: 53px; }
  .headline--alarm { top: 322px; font-size: 68px; letter-spacing: 3px; }
</style>
</head>
<body>
<main class="sheet">
  <section class="sticker sticker--deep">
    <div class="sticker__panel">
      <div class="sticker__map" role="img" aria-label="Soft blue street map background"></div>
      <svg class="sticker__signal" width="384" height="561" viewBox="0 0 384 561" aria-hidden="true">
        <circle cx="192" cy="509" r="135" fill="var(--halo)"/>
        <circle cx="192" cy="509" r="90" fill="var(--halo)"/>
        <path d="M44 496 A148 148 0 0 1 340 496" fill="none" stroke="var(--ring)" stroke-width="4"/>
        <path d="M100 496 A92 92 0 0 1 284 496" fill="none" stroke="var(--ring)" stroke-width="4"/>
        <path d="M150 496 A42 42 0 0 1 234 496" fill="none" stroke="var(--ring)" stroke-width="3"/>
        <circle cx="192" cy="509" r="34" fill="var(--accent)"/>
        <path d="M192 490 c-8 0 -13 6 -13 13 c0 9 13 22 13 22 s13 -13 13 -22 c0 -7 -5 -13 -13 -13z" fill="#fff"/>
        <circle cx="192" cy="503" r="4.5" fill="var(--accent)"/>
      </svg>
      <div class="brand">
        <span class="brand__square"></span>
        <span class="brand__name">Volmira</span>
      </div>
      <div class="headline headline--gps">GPS</div>
      <div class="headline headline--tracking">TRACKING</div>
      <div class="headline headline--alarm">ALARM</div>
    </div>
  </section>

  <section class="sticker sticker--bright">
    <div class="sticker__panel">
      <div class="sticker__map" role="img" aria-label="Soft blue street map background"></div>
      <svg class="sticker__signal" width="384" height="561" viewBox="0 0 384 561" aria-hidden="true">
        <circle cx="192" cy="509" r="135" fill="var(--halo)"/>
        <circle cx="192" cy="509" r="90" fill="var(--halo)"/>
        <path d="M44 496 A148 148 0 0 1 340 496" fill="none" stroke="var(--ring)" stroke-width="4"/>
        <path d="M100 496 A92 92 0 0 1 284 496" fill="none" stroke="var(--ring)" stroke-width="4"/>
        <path d="M150 496 A42 42 0 0 1 234 496" fill="none" stroke="var(--ring)" stroke-width="3"/>
        <circle cx="192" cy="509" r="34" fill="var(--accent)"/>
        <path d="M192 490 c-8 0 -13 6 -13 13 c0 9 13 22 13 22 s13 -13 13 -22 c0 -7 -5 -13 -13 -13z" fill="#fff"/>
        <circle cx="192" cy="503" r="4.5" fill="var(--accent)"/>
      </svg>
      <div class="brand">
        <span class="brand__square"></span>
        <span class="brand__name">Volmira</span>
      </div>
      <div class="headline headline--gps">GPS</div>
      <div class="headline headline--tracking">TRACKING</div>
      <div class="headline headline--alarm">ALARM</div>
    </div>
  </section>
</main>
</body>
</html>
```